business card for a massage therapy practice named 'Meadow and Willow Massage Studio'

I really need a trendy, yet easy on the eyes business card to complement my logo. Ideally with some gold or rose gold foil work.

My uploaded file of the logo I have in horizontal but I have a vertical version as well. Another color that is used in the website is a blush pink here and there. I'd like to see some trendy tropical leaves in the design.

```html
<!DOCTYPE html>
<html lang="en">
<head>
<meta charset="utf-8">
<title>Meadow and Willow Massage Studio – Business Card</title>
<link href="https://fonts.googleapis.com/css2?family=Questrial&display=swap" rel="stylesheet">
<style>
  :root {
    --page: #ffffff;
    --sand: #eedcb3;
    --blush: #f7d6e7;
    --ink: #1d1a17;
    --gold: #b98f35;
    --gold-light: #e3c47a;
    --leaf-dark: #3a3a2a;
    --leaf-green: #5b7d59;
    --leaf-orange: #ef7a24;
    --leaf-red: #e2294b;
  }
  * { margin: 0; padding: 0; box-sizing: border-box; }
  html, body { width: 1200px; height: 1200px; overflow: hidden; background: var(--page); }
  body { position: relative; font-family: "Questrial", "Century Gothic", sans-serif; color: var(--ink); }

  .card { position: absolute; left: 294px; width: 612px; height: 374px; overflow: hidden; }
  .card--front { top: 198px; background: var(--sand); }
  .card--back { top: 628px; background: var(--blush); }

  .art { position: absolute; display: block; }

  .art--front-leaves { left: 380px; top: 0; width: 132px; height: 104px;
    background: radial-gradient(ellipse at 50% 40%, rgba(239,122,36,.55), rgba(91,125,89,.35) 55%, rgba(238,220,179,0) 75%); }
  .art--front-flowers { left: 310px; top: 58px; width: 302px; height: 316px;
    background: radial-gradient(ellipse 95% 95% at 100% 100%, rgba(185,143,53,.75), rgba(227,196,122,.55) 45%, rgba(58,58,42,.25) 70%, rgba(238,220,179,0) 100%); }
  .art--back-leaf-orange { left: 0; top: 0; width: 104px; height: 90px;
    background: radial-gradient(ellipse 100% 100% at 0 0, rgba(239,122,36,.7), rgba(239,122,36,0) 100%); }
  .art--back-leaf-red { left: 536px; top: 120px; width: 76px; height: 66px;
    background: radial-gradient(ellipse 100% 100% at 100% 50%, rgba(226,41,75,.7), rgba(226,41,75,0) 100%); }
  .art--back-flowers { left: 0; top: 256px; width: 612px; height: 118px;
    background: radial-gradient(ellipse 60% 110% at 50% 100%, rgba(185,143,53,.8), rgba(227,196,122,.55) 45%, rgba(58,58,42,.25) 80%, rgba(247,214,231,0) 100%); }

  .brand { position: absolute; display: flex; align-items: center; gap: 12px; color: var(--ink); }
  .brand__mark { border-radius: 50%; background: var(--gold); flex: none; }
  .brand__name { line-height: 1.15; }

  .card--front .brand { left: 32px; top: 36px; }
  .card--front .brand__mark { width: 30px; height: 30px; }
  .card--front .brand__name { font-size: 25px; }

  .card--back .brand { left: 0; right: 0; top: 80px; justify-content: center; }
  .card--back .brand__mark { width: 44px; height: 44px; }
  .card--back .brand__name { font-size: 34px; }

  .person { position: absolute; left: 42px; top: 174px; font-size: 28px; font-weight: 400; letter-spacing: -0.3px; }

  .contacts { position: absolute; left: 42px; top: 228px; list-style: none; }
  .contacts li { display: flex; align-items: center; height: 33px; font-size: 18px; }
  .contacts svg { width: 16px; height: 16px; margin-right: 13px; fill: var(--ink); flex: none; }

  .socials { position: absolute; left: 0; right: 0; top: 208px; display: flex; justify-content: center; gap: 20px; font-size: 16px; }
  .socials span { display: flex; align-items: center; gap: 8px; }
  .socials i { width: 26px; height: 26px; border-radius: 50%; background: var(--gold); display: block; }
</style>
</head>
<body>

<section class="card card--front">
  <div class="art art--front-leaves" role="img" aria-label="Orange and green tropical leaves illustration"></div>
  <div class="art art--front-flowers" role="img" aria-label="Gold roses with dark tropical foliage illustration"></div>

  <div class="brand">
    <span class="brand__mark"></span>
    <span class="brand__name">Meadow and Willow<br>Massage Studio</span>
  </div>

  <h1 class="person">Marisol Vega LMT</h1>

  <ul class="contacts">
    <li><svg viewBox="0 0 24 24"><path d="M6.6 10.8a15.1 15.1 0 0 0 6.6 6.6l2.2-2.2c.3-.3.7-.4 1-.2 1.1.4 2.3.6 3.6.6.6 0 1 .4 1 1V20c0 .6-.4 1-1 1A17 17 0 0 1 3 4c0-.6.4-1 1-1h3.5c.6 0 1 .4 1 1 0 1.3.2 2.5.6 3.6.1.3 0 .7-.2 1z"/></svg>555.014.2738</li>
    <li><svg viewBox="0 0 24 24"><path d="M5 2 L19 14 L12.5 14.5 L16 22 L13 23 L9.7 15.6 L5 20Z"/></svg>meadowandwillow.com</li>
    <li><svg viewBox="0 0 24 24"><path d="M1 5h22v14H1z M3 7l9 6 9-6"/></svg>hello@meadowandwillow.com</li>
  </ul>
</section>

<section class="card card--back">
  <div class="art art--back-leaf-orange" role="img" aria-label="Orange palm leaf illustration"></div>
  <div class="art art--back-leaf-red" role="img" aria-label="Red tropical leaf illustration"></div>
  <div class="art art--back-flowers" role="img" aria-label="Gold roses with dark tropical foliage illustration"></div>

  <div class="brand">
    <span class="brand__mark"></span>
    <span class="brand__name">Meadow and Willow<br>Massage Studio</span>
  </div>

  <div class="socials">
    <span><i></i>@meadowandwillow</span>
    <span><i></i>@meadowandwillow</span>
  </div>
</section>

</body>
</html>
```